Letterhead Design Project

Professional but modern letterhead.

Target Market(s)

mining companies

Industry/Entity Type

It Professional

Colors

Designer to choose colors to be used in the design.

```html
<!DOCTYPE html>
<html lang="en">
<head>
<meta charset="utf-8">
<title>KORVA Letterhead</title>
<link href="https://fonts.googleapis.com/css2?family=Arimo:ital,wght@0,400;0,700;1,400&family=Open+Sans:wght@400&display=swap" rel="stylesheet">
<style>
  :root {
    --backdrop: #ececec;
    --paper: #fbfbfb;
    --brand-blue: #0f4c9c;
    --brand-deep: #0b3f8a;
    --cover-light: #1d68c6;
    --cover-dark: #0e4ea4;
    --body-text: #4a4a4a;
    --ink: #1e1e1e;
    --white: #ffffff;
  }
  * { margin: 0; padding: 0; box-sizing: border-box; }
  html, body { width: 1200px; height: 793px; overflow: hidden; background: var(--backdrop); }
  .canvas { position: relative; width: 1200px; height: 793px; }

  .letterhead {
    position: absolute; left: 93px; top: 66px; width: 465px; height: 660px;
    background: var(--paper); overflow: hidden;
    font-family: "Arimo", Arial, sans-serif;
  }
  .brand-name {
    position: absolute; left: 48px; top: 80px;
    font-family: "Arimo", Arial, sans-serif; font-weight: 700;
    font-size: 28px; letter-spacing: 1px; color: var(--brand-blue);
  }
  .contact-list {
    position: absolute; left: 304px; top: 27px; list-style: none;
    font-family: "Open Sans", Arial, sans-serif; font-size: 8.4px; line-height: 11px; color: #333;
  }
  .contact-list li { display: flex; align-items: flex-start; gap: 5px; }
  .contact-list li.address { margin-bottom: 2px; }
  .contact-icon { width: 8px; height: 8px; flex: none; margin-top: 1.5px; }

  .letter-date, .salutation, .letter-body p {
    position: absolute; left: 47px; width: 370px;
    font-style: italic; font-size: 8.8px; line-height: 14px; color: var(--body-text);
  }
  .letter-date { top: 160px; }
  .salutation { top: 188px; }
  .letter-body p { text-align: justify; }
  .letter-body p.first { top: 216px; }
  .letter-body p.second { top: 326px; }

  .signature-area {
    position: absolute; left: 46px; top: 470px; width: 76px; height: 48px;
    background: linear-gradient(90deg, #efefef, #e4e4e4); border-radius: 4px;
  }
  .signer-name { position: absolute; left: 47px; top: 526px; font-style: italic; font-size: 9.5px; color: #444; }
  .signer-title { position: absolute; left: 47px; top: 541px; font-size: 8.4px; color: var(--ink); }

  .footer-wave { position: absolute; left: 0; bottom: 0; width: 465px; height: 90px; }

  .cover {
    position: absolute; left: 641px; top: 66px; width: 465px; height: 660px;
    background: radial-gradient(ellipse at 50% 45%, var(--cover-light) 0%, var(--cover-dark) 75%);
  }
  .cover-brand {
    position: absolute; left: 0; right: 0; top: 310px; text-align: center;
    font-family: "Arimo", Arial, sans-serif; font-weight: 700;
    font-size: 58px; letter-spacing: 3px; color: var(--white);
  }
</style>
</head>
<body>
<div class="canvas">

  <section class="letterhead">
    <div class="brand-name">KORVA</div>

    <ul class="contact-list">
      <li class="address">
        <svg class="contact-icon" viewBox="0 0 10 10"><circle cx="5" cy="5" r="5" fill="var(--brand-blue)"/><path d="M2.5 5.2 5 3l2.5 2.2V7.5h-5z" fill="#fff"/></svg>
        <span>Suite # 410, Ore Bldg,<br>CO 80291</span>
      </li>
      <li>
        <svg class="contact-icon" viewBox="0 0 10 10"><circle cx="5" cy="5" r="5" fill="var(--brand-blue)"/><path d="M3.3 2.6c.4-.3.8 0 1 .5l.3.7c.1.3-.1.5-.3.7.3.7.7 1.1 1.3 1.4.2-.2.4-.4.7-.3l.7.3c.5.2.7.6.4 1-.5.6-1.3.7-2.2.1C4 6.3 3.3 5.4 2.9 4.4c-.3-.7-.1-1.4.4-1.8z" fill="#fff"/></svg>
        <span>555-010-2231</span>
      </li>
      <li>
        <svg class="contact-icon" viewBox="0 0 10 10"><circle cx="5" cy="5" r="5" fill="var(--brand-blue)"/><rect x="3.4" y="2.2" width="3.2" height="5.6" rx=".6" fill="#fff"/></svg>
        <span>555-010-4478</span>
      </li>
      <li>
        <svg class="contact-icon" viewBox="0 0 10 10"><circle cx="5" cy="5" r="5" fill="var(--brand-blue)"/><rect x="2.5" y="4" width="5" height="3" fill="#fff"/><rect x="3.4" y="2.5" width="3.2" height="1.6" fill="#fff"/></svg>
        <span>555-010-6602</span>
      </li>
      <li>
        <svg class="contact-icon" viewBox="0 0 10 10"><circle cx="5" cy="5" r="5" fill="var(--brand-blue)"/><rect x="2.4" y="3.2" width="5.2" height="3.6" fill="#fff"/><path d="M2.4 3.2 5 5.3l2.6-2.1" fill="none" stroke="var(--brand-blue)" stroke-width=".6"/></svg>
        <span>info@korvamail.com</span>
      </li>
      <li>
        <svg class="contact-icon" viewBox="0 0 10 10"><circle cx="5" cy="5" r="5" fill="var(--brand-blue)"/><circle cx="5" cy="5" r="2.6" fill="none" stroke="#fff" stroke-width=".7"/><path d="M2.4 5h5.2M5 2.4v5.2" stroke="#fff" stroke-width=".6"/></svg>
        <span>www.korvamail.com</span>
      </li>
    </ul>

    <p class="letter-date">December 16, 2013</p>
    <p class="salutation">To the Former Stockholders of Stellan, Inc.:</p>

    <div class="letter-body">
      <p class="first">We welcome you as shareholders of Halvern Systems Incorporated (EXCH : HLVN).We are pleased to inform you that on September 1, 2009, Stellan, Inc. (“Stellan”) merged with a subsidiary of Halvern Systems Incorporated (“Halvern Systems”). As a result of the merger, each share of Stellan preferred stock owned by you at the time of the merger was converted into and represents the right to receive the applicable Consideration Per Share, as defined in the Agreement and Plan of Merger, plus cash in lieu of any fractional shares of Halvern Systems Common Stock, if any.</p>
      <p class="second">Please read and follow carefully the enclosed instructions. In order to receive your Halvern Systems stock certificate and cash payment for your shares, if any, you must complete, sign, date and return the enclosed Letter of Transmittal, together with your Stellan stock certificate(s) in accordance with the provisions of the Letter of Transmittal and the enclosed instructions. Each person listed on your Stellan stock certificate(s) as a registered holder must sign the Letter of Transmittal. You should complete and sign a separate Letter of Transmittal for each certificate registered in a different name or form. Photocopies of the Letter of Transmittal may be used. If you have any questions, please contact the exchange agent, Northgate Share Registry Company, LLC, toll free at<br>(555) 010–4417 or at (555) 010–8317.</p>
    </div>

    <div class="signature-area" role="img" aria-label="Handwritten signature of the managing director"></div>
    <p class="signer-name">Dana Mercer</p>
    <p class="signer-title">Managing Director</p>

    <svg class="footer-wave" viewBox="0 0 465 90" preserveAspectRatio="none">
      <path d="M0 8 C110 20 250 42 340 30 C395 23 440 22 465 34 L465 90 L0 90 Z" fill="var(--brand-blue)"/>
      <path d="M0 36 C140 90 300 72 465 38 L465 90 L0 90 Z" fill="var(--brand-deep)"/>
      <path d="M0 34 C140 88 300 70 465 36" fill="none" stroke="var(--white)" stroke-width="3"/>
    </svg>
  </section>

  <section class="cover">
    <div class="cover-brand">KORVA</div>
  </section>

</div>
</body>
</html>
```